依頼詳細
安くて簡単に発注が出来ることをアピールしたいと思っております。
記載項目
ラフを添付しておりますのでご確認ください。配置や文章などより分かりやすいデザインがある場合はラフ通りでなくても問題ございません。あくまで素人がラフを作成しましたので・・ラフはモノクロですがカラーの明るいイメージでお願いします

また納期がタイトなため、日曜日までの受付とさせていただき、月曜日にデータ納品が出来る方でお願いします。
サイズ
A4
ページ数
両面
希望イメージ
シンプル 複雑
単色 カラフル
暗い 明るい
日常 高級
遊び心 厳粛
未来的 伝統的
女性的 男性的
希望する色
弊社サイトがオレンジの為、オレンジと白を基調にお願いします。
納品ファイル
• 高解像度JPG (.jpg)
• イラストレーター形式 (.ai)
補足説明
弊社サイトは下記URLになります。
http://krvprint.net
選定確約に変更させて頂きます。

また、月曜日までの納品は必須になってしまいますので、修正がある場合などは締め切り時間(7月7日の18時頃)30分後までには修正依頼をお願いすることになります。修正を依頼するのは確定する方1名とさせて頂きます。

修正が完了されましたら完了したデータを納品して頂ければ確定させて頂きます。
納期タイトで大変申し訳ございませんが多くの応募をお待ちしております。

```html
<!DOCTYPE html>
<html lang="ja">
<head>
<meta charset="UTF-8">
<title>名刺発注のご案内</title>
<link href="https://fonts.googleapis.com/css2?family=M+PLUS+Rounded+1c:wght@500;700;800&display=swap" rel="stylesheet">
<style>
  :root {
    --bg-orange: #f6a13a;
    --bg-orange-light: #f9b356;
    --white: #ffffff;
    --ink: #1d1d1d;
    --accent-red: #e8261e;
    --zero-pink: #f7c7c3;
  }
  * { margin: 0; padding: 0; box-sizing: border-box; }
  html, body { width: 846px; height: 1200px; overflow: hidden; }
  body {
    position: relative;
    background: linear-gradient(180deg, var(--bg-orange-light), var(--bg-orange) 40%);
    font-family: "M PLUS Rounded 1c", sans-serif;
    font-weight: 700;
    color: var(--ink);
  }
  .abs { position: absolute; white-space: nowrap; }
  .headline-lead { left: 34px; top: 46px; font-size: 38px; color: var(--white); }
  .headline-main { left: 190px; top: 62px; font-size: 60px; color: var(--accent-red); font-weight: 800; letter-spacing: 2px; }
  .headline-rule { left: 176px; top: 138px; width: 576px; height: 4px; background: var(--white); }
  .headline-tail { right: 44px; top: 160px; font-size: 38px; color: var(--white); }
  .section-title { left: 34px; font-size: 30px; color: var(--white); }
  .price-grid {
    left: 34px; top: 333px; width: 784px; height: 124px;
    display: grid; grid-template-columns: repeat(6, 1fr);
    border: 4px solid var(--ink);
  }
  .price-grid span { border-right: 4px solid var(--ink); }
  .price-grid span:last-child { border-right: none; }
  .body-text { font-size: 28px; color: var(--white); }
  .old-fee { left: 96px; top: 556px; font-size: 28px; line-height: 37px; }
  .old-fee .amount { display: inline-block; width: 130px; text-align: right; }
  .strike { left: 200px; top: 560px; }
  .fee-arrow { left: 520px; top: 580px; }
  .free-zero { left: 660px; top: 490px; font-size: 150px; color: var(--zero-pink); font-weight: 500; line-height: 1; }
  .free-yen { left: 752px; top: 588px; font-size: 36px; color: var(--zero-pink); }
  .free-note { left: 657px; top: 664px; font-size: 12px; line-height: 16px; color: var(--ink); white-space: normal; width: 180px; font-weight: 500; }
  .revision-text { left: 96px; top: 660px; line-height: 37px; color: var(--white); font-size: 28px; }
  .shipping { left: 147px; top: 866px; font-size: 28px; line-height: 43px; }
  .shipping li { list-style: none; display: flex; }
  .shipping .carrier { width: 380px; }
  .shipping .arrow { width: 90px; }
  .shipping .price { width: 200px; text-align: right; }
  .back-note { right: 30px; top: 1150px; font-size: 28px; color: var(--ink); }
</style>
</head>
<body>
  <div class="abs headline-lead">名刺が</div>
  <div class="abs headline-main">安く！　簡単に！</div>
  <div class="abs headline-rule"></div>
  <div class="abs headline-tail">発注できます！</div>

  <div class="abs section-title" style="top:276px">・Vectra Drawでの入稿価格（上質紙の場合）</div>
  <div class="abs price-grid"><span></span><span></span><span></span><span></span><span></span><span></span></div>

  <div class="abs section-title" style="top:490px">・現物名刺からは出来ないの？</div>
  <div class="abs old-fee">データ製作料が片面<span class="amount">1,000円</span><br><span style="padding-left:196px">両面</span><span class="amount">2,000円</span></div>
  <svg class="abs strike" width="230" height="80" viewBox="0 0 230 80">
    <line x1="60" y1="8" x2="220" y2="74" stroke="#1d1d1d" stroke-width="2"/>
  </svg>
  <svg class="abs fee-arrow" width="120" height="40" viewBox="0 0 120 40">
    <line x1="4" y1="20" x2="100" y2="20" stroke="#e8261e" stroke-width="5"/>
    <polygon points="96,8 118,20 96,32" fill="#e8261e"/>
  </svg>
  <div class="abs free-zero">0</div>
  <div class="abs free-yen">円</div>
  <div class="abs free-note">※ただし、デザインが複雑な場合別途費用が発生する場合がございます。</div>
  <div class="abs revision-text">しかも、一度弊社で作成された<br>デザインの文字修正無料！</div>

  <div class="abs section-title" style="top:762px">・他にかかる費用は？</div>
  <ul class="abs shipping">
    <li><span class="carrier">ヤマビコメール</span><span class="arrow">→</span><span class="price">180円（税込）</span></li>
    <li><span class="carrier">ヤマビコ速達メール便</span><span class="arrow">→</span><span class="price">280円（税込）</span></li>
    <li><span class="carrier">佐野川宅配便</span><span class="arrow">→</span><span class="price">380円（税込）</span></li>
  </ul>

  <div class="abs section-title" style="top:1016px">・既存のサンプル</div>

  <div class="abs back-note">依頼方法はウラ面へ→</div>
</body>
</html>
```